Brook 4 Brook letterhead design and business card design for electrical company

I need a letterhead that can be used for my invoices and quote books along with emails sent to clients. I have a logo and the logo of Volt Guild I just need all my information placed nicely with a good flow.

Business Name: Brook 4 Brook Electrical
Name: Daniel Karvounis
Abn: 58917204316
Licence Number: 67413
Number: 0400583641

Thank you in advanced

Target Market(s)

Electrical Clients

Industry/Entity Type

Business

Contact Information for Business Card

Name: Daniel Karvounis
Abn: 58917204316
Licence Number: 67413
Number: 0400583641

Font styles to use
Sans Serif

Colors

Designer to choose colors to be used in the design.

Requirements
Must have
• Must have my logo, volt guild logo even if its smaller and in the corner and all details
Nice to have
• Domestic Commercial Industrial stated on there somewhere

```html
<!DOCTYPE html>
<html lang="en">
<head>
<meta charset="UTF-8">
<title>Brook 4 Brook Electrical – Business Card</title>
<link rel="stylesheet" href="https://fonts.googleapis.com/css2?family=Roboto+Slab:wght@300;400;500&display=swap">
<style>
  :root {
    --backdrop: #cfb15a;
    --card-dark: #131719;
    --card-light: #ffffff;
    --brand-blue: #2472ce;
    --brand-grey: #bac6c5;
    --ink: #141414;
  }
  * { margin: 0; padding: 0; box-sizing: border-box; }
  html, body {
    width: 1200px;
    height: 1067px;
    overflow: hidden;
    background: var(--backdrop);
    font-family: "Roboto Slab", Georgia, serif;
  }
  .card {
    position: absolute;
    overflow: hidden;
  }
  .card-front {
    left: 268px; top: 81px;
    width: 664px; height: 398px;
    background: var(--card-dark);
  }
  .brand {
    position: absolute;
    left: 0; right: 0; top: 176px;
    display: flex;
    align-items: center;
    justify-content: center;
    gap: 12px;
  }
  .brand-dot {
    width: 16px; height: 16px;
    border-radius: 50%;
    background: var(--brand-blue);
  }
  .brand-name {
    color: var(--brand-blue);
    font-weight: 500;
    font-size: 34px;
    letter-spacing: 0.5px;
    line-height: 1;
  }
  .card-back {
    left: 268px; top: 588px;
    width: 664px; height: 398px;
    background: var(--card-light);
    color: var(--ink);
  }
  .holder-name {
    position: absolute;
    top: 100px; left: 0; right: 0;
    text-align: center;
    font-size: 23px;
    font-weight: 300;
    line-height: 1.2;
  }
  .name-rule {
    position: absolute;
    top: 135px; left: 283px;
    width: 97px; height: 2px;
    background: var(--ink);
  }
  .phone-line {
    position: absolute;
    top: 154px; left: 0; right: 0;
    display: flex;
    justify-content: center;
    align-items: center;
    gap: 4px;
    font-size: 19px;
    font-weight: 300;
  }
  .phone-icon { width: 42px; height: 40px; }
  .id-line {
    position: absolute;
    top: 219px; left: 0; right: 0;
    display: flex;
    justify-content: center;
    align-items: center;
    gap: 10px;
    font-size: 19px;
    font-weight: 300;
  }
  .id-divider {
    width: 2px; height: 27px;
    background: var(--ink);
  }
  .corner-bands {
    position: absolute;
    left: 0; top: 0;
    width: 664px; height: 398px;
  }
</style>
</head>
<body>
  <section class="card card-front" aria-label="Card front">
    <div class="brand">
      <span class="brand-dot"></span>
      <span class="brand-name">Brook 4 Brook</span>
    </div>
  </section>

  <section class="card card-back" aria-label="Card back">
    <svg class="corner-bands" viewBox="0 0 664 398" aria-hidden="true">
      <polygon points="385,357 664,297 664,398 385,398" fill="var(--brand-grey)"/>
      <polygon points="0,264 555,398 0,398" fill="var(--brand-blue)"/>
    </svg>

    <h1 class="holder-name">Daniel Karvounis</h1>
    <div class="name-rule"></div>

    <p class="phone-line">
      <svg class="phone-icon" viewBox="0 0 42 40" aria-hidden="true">
        <path d="M6 8c2-2 5-2 6 0l3 5c1 2 0 3-1 4l-2 2c2 4 5 7 9 9l2-2c1-1 2-2 4-1l5 3c2 1 2 4 0 6l-2 2c-3 3-10 1-17-6S3 13 6 8z" fill="var(--brand-grey)"/>
        <ellipse cx="29" cy="8" rx="9" ry="7" fill="var(--brand-grey)"/>
        <polygon points="24,13 22,19 28,14" fill="var(--brand-grey)"/>
        <circle cx="25.5" cy="8" r="1.3" fill="#fff"/>
        <circle cx="29" cy="8" r="1.3" fill="#fff"/>
        <circle cx="32.5" cy="8" r="1.3" fill="#fff"/>
      </svg>
      <span>Ph. Number: 0400583641</span>
    </p>

    <p class="id-line">
      <span>Abn: 58917204316</span>
      <span class="id-divider"></span>
      <span>Licence Number: 67413</span>
    </p>
  </section>
</body>
</html>
```